Business Card, Letterhead, Envelopes, Thank you cards, Post Cards
Business cards and stationary for life coach
Professional
Silver Heron Guidance Studio
Marla Penrick, MA
4810 North Calloway Avenue
Suite C 240
Missoula, Montana 59417
silverheronguidance@mailbox-example.net
silverheronguidance-example.com
I would like to see 'Let Your Dreams Take Flight' on the front of the card. This is the tagline. Please use a compatible font with the logo.
'Dragonfly spends most of her life underwater until the day she discovers her wings and soars upon the wind.' I'd like to see this in script, similar to the logo font.
Please let me know if you need different files.

```html
<!DOCTYPE html>
<html lang="en">
<head>
<meta charset="utf-8">
<title>Silver Heron Guidance Studio – Business Cards</title>
<link rel="stylesheet" href="https://fonts.googleapis.com/css2?family=Montserrat:wght@400;500;600;700&display=swap">
<style>
  :root {
    --bg: #2b2d30;
    --label: #d6d8db;
    --card-light: #f4f5f6;
    --card-shade: #d9dcdf;
    --ink: #2a2f35;
    --brand-blue: #1d63ad;
    --sky-blue: #35a7dd;
    --back-blue: #1a5aa3;
    --band-blue: #3a7cc4;
    --white: #ffffff;
  }
  * { margin: 0; padding: 0; box-sizing: border-box; }
  html, body { width: 1200px; height: 799px; overflow: hidden; }
  body {
    background: var(--bg);
    font-family: "Montserrat", Arial, sans-serif;
    position: relative;
  }
  .sheet-label {
    position: absolute;
    left: 403px;
    color: var(--label);
    font-size: 16px;
    font-weight: 600;
    white-space: nowrap;
  }
  .label-front { top: 68px; }
  .label-back { top: 424px; }
  .card {
    position: absolute;
    left: 391px;
    width: 466px;
    border-radius: 16px;
    overflow: hidden;
  }
  .card-front {
    top: 100px;
    height: 274px;
    background: linear-gradient(135deg, var(--card-light) 0%, var(--white) 45%, var(--card-shade) 100%);
  }
  .faint-art {
    position: absolute;
    left: 20px;
    top: 70px;
    width: 150px;
    height: 200px;
    border-radius: 50%;
    background: radial-gradient(ellipse, rgba(150,155,160,0.22), rgba(150,155,160,0) 70%);
  }
  .corner-art {
    position: absolute;
    left: 335px;
    top: 4px;
    width: 120px;
    height: 90px;
    border-radius: 50%;
    background: radial-gradient(ellipse, rgba(53,167,221,0.35), rgba(53,167,221,0) 70%);
  }
  .holder-name {
    position: absolute;
    left: 178px;
    top: 20px;
    color: var(--brand-blue);
    font-size: 20px;
    font-weight: 700;
    white-space: nowrap;
  }
  .brand-name {
    position: absolute;
    left: 182px;
    top: 80px;
    color: var(--brand-blue);
    font-size: 18px;
    font-weight: 600;
    white-space: nowrap;
  }
  .tagline {
    position: absolute;
    left: 183px;
    top: 108px;
    color: var(--sky-blue);
    font-size: 10px;
    font-weight: 600;
    letter-spacing: 0.8px;
    text-transform: uppercase;
    white-space: nowrap;
  }
  .address {
    position: absolute;
    left: 185px;
    top: 152px;
    color: var(--ink);
    font-size: 12px;
    font-style: normal;
    line-height: 17px;
    white-space: nowrap;
  }
  .contact {
    position: absolute;
    left: 185px;
    top: 205px;
    color: var(--ink);
    font-size: 11px;
    line-height: 17px;
    list-style: none;
    white-space: nowrap;
  }
  .contact li { display: flex; align-items: center; gap: 6px; }
  .contact svg { width: 11px; height: 11px; fill: var(--ink); flex: none; }
  .card-back {
    top: 466px;
    height: 264px;
    background: var(--back-blue);
  }
  .wing-art {
    position: absolute;
    left: 215px;
    top: 8px;
    width: 120px;
    height: 130px;
    border-radius: 50%;
    background: radial-gradient(ellipse, rgba(255,255,255,0.32), rgba(255,255,255,0) 70%);
  }
  .back-brand {
    position: absolute;
    left: 30px;
    top: 112px;
    color: var(--white);
    font-size: 24px;
    font-weight: 600;
    white-space: nowrap;
  }
  .quote-band {
    position: absolute;
    left: 0; right: 0; bottom: 0;
    height: 88px;
    background: var(--band-blue);
    padding: 9px 30px;
    color: var(--white);
    font-size: 12px;
    line-height: 23px;
  }
</style>
</head>
<body>
  <p class="sheet-label label-front">Business Cards (front)</p>
  <section class="card card-front">
    <div class="faint-art" role="img" aria-label="Faint grey dragonfly illustration"></div>
    <div class="corner-art" role="img" aria-label="Blue dragonfly illustration"></div>
    <h1 class="holder-name">Marla Penrick, MA</h1>
    <p class="brand-name">Silver Heron Guidance Studio</p>
    <p class="tagline">Let Your Dreams Take Flight</p>
    <address class="address">
      4810 North Calloway Avenue<br>
      Suite C 240<br>
      Missoula, Montana 59417
    </address>
    <ul class="contact">
      <li><svg viewBox="0 0 12 12"><path d="M1 4c0-2 2-3 5-3s5 1 5 3l-2 1-1-1H4L3 5 1 4zm2 2h6l1 5H2l1-5z"/></svg>406-555-0172</li>
      <li><svg viewBox="0 0 12 12"><path d="M0 2h12v1.2L6 7 0 3.2zM0 4.6l6 3.8 6-3.8V10H0z"/></svg>silverheronguidance@mailbox-example.net</li>
      <li><svg viewBox="0 0 12 12"><circle cx="6" cy="6" r="5.5"/></svg>silverheronguidance-example.com</li>
    </ul>
  </section>

  <p class="sheet-label label-back">Business Cards (Back)</p>
  <section class="card card-back">
    <div class="wing-art" role="img" aria-label="White dragonfly illustration"></div>
    <p class="back-brand">Silver Heron Guidance Studio</p>
    <blockquote class="quote-band">'Dragonfly spends most of her life underwater until the day she discovers her wings and soars upon the wind.' I'd like to see this in script, similar to the logo font.</blockquote>
  </section>
</body>
</html>
```